KLMR stationery 2023

Our stationery dates back to 2007 when we changed practice rooms.
We would like to have kept the logo and spiced up the design, especially since we have one more colleague (Dr. Henriette Bollmeyer)
Our practice colors are a slightly more muted pink and sand-colored.
Follow-up orders for flyers, notices, etc. are still waiting for this design.

```html
<!DOCTYPE html>
<html lang="de">
<head>
<meta charset="utf-8">
<title>KLMR Briefpapier</title>
<link rel="stylesheet" href="https://fonts.googleapis.com/css2?family=Arimo:wght@400;700&family=Source+Sans+3:wght@400&display=swap">
<style>
  :root {
    --bg: #dedede;
    --paper: #ffffff;
    --ink: #1c1c1e;
    --text: #8a8a8a;
    --text-dark: #5e5e5e;
    --pink: #ee3ad8;
    --teal: #bfe8ea;
    --band: #1c1c1e;
  }
  * { box-sizing: border-box; margin: 0; padding: 0; }
  html, body { width: 1200px; height: 1200px; overflow: hidden; background: var(--bg); }
  .letterhead {
    position: absolute; left: 190px; top: 20px;
    width: 820px; height: 1160px; background: var(--paper);
    font-family: "Arimo", Arial, sans-serif; color: var(--text);
  }
  .brand { position: absolute; left: 71px; top: 50px; display: flex; align-items: center; gap: 10px; }
  .brand-mark { width: 26px; height: 26px; background: var(--pink); }
  .brand-name { font-size: 52px; font-weight: 400; color: var(--ink); letter-spacing: 2px; line-height: 1; }
  .doctors {
    position: absolute; left: 595px; top: 40px; padding-left: 12px;
    border-left: 2px solid var(--pink); list-style: none;
    font-size: 14px; line-height: 16.5px; color: var(--text-dark);
  }
  .salutation {
    position: absolute; left: 75px; top: 354px;
    font-family: "Source Sans 3", sans-serif; font-size: 18px; color: var(--text);
  }
  .body-copy { position: absolute; left: 73px; top: 410px; width: 672px; font-size: 13.7px; line-height: 16.8px; }
  .body-copy p { margin-bottom: 15px; }
  .closing { position: absolute; left: 75px; top: 753px; font-family: "Source Sans 3", sans-serif; font-size: 10px; }
  .signature { position: absolute; left: 76px; top: 808px; width: 104px; height: 30px; background: linear-gradient(90deg, #d6d6d6, #ececec); }
  .hours {
    position: absolute; left: 50px; top: 1001px; width: 722px;
    display: flex; align-items: center; gap: 6px;
    font-size: 13.6px; font-weight: 700; color: var(--text-dark); white-space: nowrap;
  }
  .hours::before, .hours::after { content: ""; flex: 1; height: 2px; background: var(--pink); }
  .footer-art { position: absolute; left: 18px; top: 1030px; width: 210px; height: 100px; background: linear-gradient(110deg, #e8f7f8, var(--teal)); }
  .contact {
    position: absolute; left: 246px; top: 1032px; height: 96px; padding-left: 15px;
    border-left: 1px solid #777; list-style: none;
    font-family: "Source Sans 3", sans-serif; font-size: 13.5px; line-height: 16.6px; color: var(--text-dark);
  }
  .contact li { display: flex; align-items: center; gap: 6px; }
  .contact .gap { margin-top: 2px; }
  .contact svg { width: 10px; height: 10px; fill: var(--pink); flex: none; }
  .services {
    position: absolute; left: 479px; top: 1032px; height: 96px; padding-left: 18px;
    border-left: 1px solid #777; list-style: none;
    font-size: 13.8px; line-height: 16.6px; color: var(--text-dark);
  }
  .services li::before { content: ""; display: inline-block; width: 5px; height: 5px; border-radius: 50%; background: var(--pink); margin: 0 4px 2px -8px; vertical-align: middle; }
  .band { position: absolute; left: 0; top: 1144px; width: 820px; height: 16px; }
</style>
</head>
<body>
  <main class="letterhead">
    <header>
      <div class="brand">
        <span class="brand-name">KLMR</span>
        <span class="brand-mark"></span>
      </div>
      <ul class="doctors">
        <li>Dr. Gisela Marwitz</li>
        <li>Dr. Petra Lindqvist</li>
        <li>Dr. Tobias Marwitz</li>
        <li>Dr. Ilona Berczi</li>
        <li>Dr. Henriette Bollmeyer</li>
      </ul>
    </header>

    <p class="salutation">Dear Mr. Smith,</p>
    <section class="body-copy">
      <p>Lorem ipsum dolor sit amet, consectetuer adipiscing elit, sed diam nonmmy nibh euismod tincidunt ut laor eet dolore magna aliquam erat volutpat. Ut wisi enim ad minim veniam, quis nostrud exerci tationmcorper suscipit lobortis nisl ut aliquip ex ea commodo consequat. Duis autem vel eum iriure dolor in hendrerit in vulputate velit esse molestie consequat, vel illum dolore eu feugiat</p>
      <p>Rorem ipsum dolor sit amet, consectetuer adipiscing elit, sed diam nonmmy nibh euismod tincidunt ut laor eet dolore magna aliquam erat volutpat. Ut wisi enim ad minim veniam, quis nostrud exerci tationmcorper suscipit lobortis nisl ut aliquip ex ea commodo consequat. Duis autem vel eum iriure dolor in hendrerit in vulputate velit esse molest</p>
      <p>Dorem ipsum dolor sit amet, consectetuer adipiscing elit, sed diam nonmmy nibh euismod tincidunt ut laor eet dolore magna aliquam erat volutpat. Ut wisi enim ad minim veniam, quis nostrud exerci tationmcorper suscipit lobortis nisl ut aliquip ex ea commodo consequat. Duis autem vel eum iriure dolor in hendrerit in suscipit lobortis nisl ut aliquip ex ea commodo consequat. Duis autem vel eum iriure dolor in hendrerit in vulputate velit esse molestie consequat, vel illum</p>
      <p>Sorem ipsum dolor sit amet, consectetuer adipiscing elit, sed diam nonmmy nibh euismod tincidunt ut laor eet dolore magna aliquam erat volutpat. Ut wisi enim ad minim veniam, quis nostrud exerci tationmcorper suscipit lobortis nisl ut aliquip ex ea commodo consequat. Duis autem vel eum iriure dolor in</p>
    </section>
    <p class="closing">Sincerely,</p>
    <div class="signature" role="img" aria-label="Handwritten signature"></div>

    <footer>
      <p class="hours">Öffnungszeiten NEU: Montag - Freitag 08.00 - 12.00 Uhr und 13.00 - 17.00 Uhr</p>
      <div class="footer-art" role="img" aria-label="Light teal line illustration of women walking beside the practice building"></div>
      <ul class="contact">
        <li>Ahornweg 14</li>
        <li>8400 Talbach</li>
        <li class="gap"><svg viewBox="0 0 10 10"><path d="M2 0h2l1 3-1.3 1a6 6 0 0 0 2.3 2.3L7 5l3 1v2a2 2 0 0 1-2 2A8 8 0 0 1 0 2a2 2 0 0 1 2-2z"/></svg>052/611 48 20</li>
        <li><svg viewBox="0 0 10 10"><rect x="0" y="4" width="10" height="6" rx="1"/><rect x="2" y="0" width="6" height="3"/></svg>052/611 48 22</li>
        <li><svg viewBox="0 0 10 10"><path d="M0 2h10v6H0z M0 2l5 3.5L10 2" stroke="#fff" stroke-width="0.8"/></svg>praxis@klmr-beispiel.ch</li>
        <li><svg viewBox="0 0 10 10"><circle cx="5" cy="5" r="5"/><path d="M0 5h10M5 0v10" stroke="#fff" stroke-width="0.8"/></svg>www.klmr-praxis.ch</li>
      </ul>
      <ul class="services">
        <li>Fachärzte für Gynäkologie und Geburtshilfe</li>
        <li>Pränataldiagnostik</li>
        <li>Schwangerschaftsbetreuung</li>
        <li>Kinderwunschbehandlung</li>
        <li>Ambulante Operationen</li>
        <li>Onkologische Betreuung</li>
      </ul>
      <svg class="band" viewBox="0 0 820 16" preserveAspectRatio="none" aria-hidden="true">
        <polygon points="0,0 612,0 598,16 0,16" fill="var(--band)"/>
        <polygon points="625,0 820,0 820,16 611,16" fill="var(--pink)"/>
      </svg>
    </footer>
  </main>
</body>
</html>
```